Business card design needed

I am a nutritionist and fitness instructor and I need a business card designed for my company CookRunGrow. I provide nutrition education services such as consultations, cooking demonstrations, workshops, and supermarket tours. I also provide fitness instruction and training to clients to help overhaul their lifestyle.

I would like to see designs that have a natural, organic, feel using earthy colours. I would like to have cards printed on recycled paper.

I would prefer a 2 sided card. Front side with just the business name Cook Run Grow and underneath Nutrition Health Fitness. The second side to have the contact details.

The final design should communicate health and wellness through eating organic wholefoods and being physically active.

Although I have this idea, I would be open to see other suggestions that have a similar look and feel.

Target Market(s)

people interested in being healthier, women wanting to loose weight, mothers wanting to be healthier for their families

Industry/Entity Type

Nutrition

Contact Information for Business Card

Megan Furlow
Nutritionist and Personal Trainer
M 0417382956
E cookrungrowwellness@mailbox-demo.net

Logo Text

CookRunGrow (underneath) Nutrition Health Fitness

Logo styles of interest
Wordmark Logo
Requirements
Nice to have
• I like the idea of having the letters of CookRunGrow spelt out with food such as grains, nuts, seeds, legumes, fruit etc. For example close up images of cherry tomatoes, chia seeds, kidney beans, chickpeas, blue berries, raspberries, brown rice - lots of different colours and textures. Continuing playing on the idea of the book cover Walk Sing Rest.

food is important - I am not selling supplements rather I am promoting the enjoyment of healthy wholefoods so food is important to the look and feel of the design
Should not have
• cartoon images
images associated with body building or supplements
fruit or dumb bells with tape measures around them
clichés for weight loss such as scales and tape measures
I don't want to look like other typical wellness services such as massage or spa services

```html
<!DOCTYPE html>
<html lang="en">
<head>
<meta charset="utf-8">
<title>Cook Run Grow Business Card</title>
<link rel="stylesheet" href="https://fonts.googleapis.com/css2?family=Open+Sans:wght@400;600&display=swap">
<style>
  :root {
    --backdrop: #e6e4e1;
    --card: #ffffff;
    --leaf-green: #7cc242;
    --berry-red: #e0262b;
    --ink: #4f5356;
    --slate: #8a8d90;
    --card-shadow: rgba(60, 55, 50, 0.22);
  }
  * { box-sizing: border-box; margin: 0; padding: 0; }
  html, body {
    width: 1200px;
    height: 800px;
    overflow: hidden;
    background: var(--backdrop);
    font-family: "Open Sans", Arial, sans-serif;
  }
  .canvas {
    position: relative;
    width: 1200px;
    height: 800px;
  }
  .card {
    position: absolute;
    top: 245px;
    width: 540px;
    height: 310px;
    background: var(--card);
    border-radius: 18px;
    overflow: hidden;
    box-shadow: 0 10px 28px var(--card-shadow);
  }
  .card--contact { left: 40px; }
  .card--brand { left: 620px; }

  .edge-band {
    position: absolute;
    left: 0;
    top: 0;
    bottom: 0;
    width: 26px;
    background: var(--leaf-green);
  }
  .edge-rule {
    position: absolute;
    left: 32px;
    top: 0;
    bottom: 0;
    width: 4px;
    background: var(--berry-red);
  }

  .wordmark {
    position: absolute;
    display: flex;
    flex-direction: column;
  }
  .wordmark__name {
    color: var(--ink);
    font-weight: 600;
    font-size: 20px;
    line-height: 1;
    letter-spacing: 3px;
    text-transform: uppercase;
  }
  .wordmark__tagline {
    margin-top: 8px;
    color: var(--slate);
    font-size: 12px;
    letter-spacing: 1px;
  }
  .card--contact .wordmark { left: 62px; top: 42px; }
  .card--brand .wordmark { left: 0; right: 0; top: 132px; align-items: center; text-align: center; }

  .person {
    position: absolute;
    right: 36px;
    top: 122px;
    text-align: right;
  }
  .person__name {
    color: var(--leaf-green);
    font-size: 30px;
    font-weight: 400;
    line-height: 1.05;
  }
  .person__role {
    color: var(--berry-red);
    font-size: 11px;
    margin-top: 4px;
  }

  .contact-list {
    position: absolute;
    right: 36px;
    top: 196px;
    list-style: none;
    text-align: right;
  }
  .contact-list__item {
    display: flex;
    justify-content: flex-end;
    align-items: center;
    gap: 8px;
    color: var(--berry-red);
    font-size: 13px;
    line-height: 23px;
  }
  .contact-list__icon { width: 14px; height: 14px; flex: none; }
</style>
</head>
<body>
<main class="canvas">

  <section class="card card--contact" aria-label="Business card, contact side">
    <div class="edge-band" aria-hidden="true"></div>
    <div class="edge-rule" aria-hidden="true"></div>

    <div class="wordmark">
      <span class="wordmark__name">Cook Run Grow</span>
      <span class="wordmark__tagline">Nutrition Health Fitness</span>
    </div>

    <div class="person">
      <h1 class="person__name">Megan Furlow</h1>
      <p class="person__role">Nutritionist and Personal Trainer</p>
    </div>

    <ul class="contact-list">
      <li class="contact-list__item">
        <span>M 0417382956</span>
        <svg class="contact-list__icon" viewBox="0 0 14 14" aria-hidden="true">
          <rect x="3.5" y="1" width="7" height="12" rx="1.5" fill="none" stroke="var(--leaf-green)" stroke-width="1.6"/>
          <circle cx="7" cy="10.6" r="0.9" fill="var(--leaf-green)"/>
        </svg>
      </li>
      <li class="contact-list__item">
        <span>cookrungrowwellness@mailbox-demo.net</span>
        <svg class="contact-list__icon" viewBox="0 0 14 14" aria-hidden="true">
          <rect x="1" y="3" width="12" height="8.5" rx="1" fill="var(--leaf-green)"/>
          <path d="M1.5,3.6 L7,8 L12.5,3.6" fill="none" stroke="var(--card)" stroke-width="1.2"/>
        </svg>
      </li>
      <li class="contact-list__item">
        <span>www.cookrungrow-demo.net</span>
        <svg class="contact-list__icon" viewBox="0 0 14 14" aria-hidden="true">
          <circle cx="7" cy="7" r="6" fill="var(--leaf-green)"/>
          <path d="M1,7 H13 M7,1 C4,4 4,10 7,13 M7,1 C10,4 10,10 7,13" fill="none" stroke="var(--card)" stroke-width="0.9"/>
        </svg>
      </li>
    </ul>
  </section>

  <section class="card card--brand" aria-label="Business card, brand side">
    <div class="wordmark">
      <span class="wordmark__name">Cook Run Grow</span>
      <span class="wordmark__tagline">Nutrition Health Fitness</span>
    </div>
  </section>

</main>
</body>
</html>
```